Corwin Ashdale Building Company, Inc.
Business Cards, Letterhead, Envelopes, Fax Cover
Professional
Miles T. Fenwick
PO Box 48217
Brookvale, NC 27000
miles@corwinashdale-example.com
www.corwinashdale-example.com
looking for a traditional style card, however nothing dated. same goes for the stationary. Something that is creative , but still shows professionalism and adaptable to the corporate environment. We don't want gloss cards. waiting on office and fax #'s. should have those in a day or two. As for the font, I put use same as logo font, but may want to see standard as well.
CA

```html
<!DOCTYPE html>
<html lang="en">
<head>
<meta charset="utf-8">
<title>Corwin Ashdale Building Company – Business Card</title>
<link href="https://fonts.googleapis.com/css2?family=Montserrat:wght@400;500&family=Open+Sans:wght@400;600&display=swap" rel="stylesheet">
<style>
  :root {
    --backdrop: #b08a2c;
    --card-white: #ffffff;
    --navy: #1f3a6e;
    --ink: #3a3a3a;
    --muted: #6b6b6b;
    --slate: #7d7d7d;
  }
  * { margin: 0; padding: 0; box-sizing: border-box; }
  html, body { width: 1200px; height: 686px; overflow: hidden; }
  body {
    background: var(--backdrop);
    position: relative;
    font-family: "Open Sans", sans-serif;
  }
  .card {
    position: absolute;
    box-shadow: 0 6px 14px rgba(0,0,0,0.35);
  }
  .card-front {
    left: 53px; top: 151px; width: 535px; height: 305px;
    background: var(--card-white);
    border-top: 9px solid var(--navy);
  }
  .card-back {
    left: 610px; top: 235px; width: 535px; height: 303px;
    background: var(--slate);
    border-top: 14px solid var(--card-white);
  }
  .card-back::before {
    content: ""; position: absolute; left: 0; right: 0; top: -14px; height: 8px;
    background: var(--navy);
  }
  .wordmark {
    position: absolute; left: 96px; top: 72px;
    display: flex; align-items: center; gap: 12px;
    font-family: "Montserrat", sans-serif; font-weight: 400;
    color: var(--navy);
  }
  .wordmark-square { width: 36px; height: 36px; background: var(--navy); }
  .wordmark-name { font-size: 29px; letter-spacing: 0.5px; line-height: 1; text-transform: uppercase; }
  .wordmark-sub { font-size: 15px; letter-spacing: 2px; line-height: 1.4; text-transform: uppercase; }
  .contact {
    position: absolute; left: 0; right: 0; top: 172px;
    text-align: center; color: var(--ink); font-size: 13px; line-height: 1.3;
  }
  .person { font-size: 15px; margin-bottom: 6px; }
  .person-name { color: var(--navy); font-weight: 600; }
  .person-sep { color: var(--muted); margin: 0 10px; }
  .person-title { color: var(--ink); }
  .address { margin-bottom: 6px; }
  .contact-row { display: flex; justify-content: center; gap: 22px; margin-bottom: 6px; }
  .contact-item { display: inline-flex; align-items: center; gap: 4px; }
  .contact-item svg { width: 12px; height: 12px; fill: var(--navy); }
  .back-mark {
    position: absolute; left: 0; right: 0; top: 120px; text-align: center;
    font-family: "Montserrat", sans-serif; font-weight: 500;
    font-size: 40px; letter-spacing: 3px; color: var(--navy);
    text-transform: uppercase;
  }
</style>
</head>
<body>
  <section class="card card-front">
    <div class="wordmark">
      <span class="wordmark-square"></span>
      <div>
        <div class="wordmark-name">Corwin Ashdale</div>
        <div class="wordmark-sub">Building Company</div>
      </div>
    </div>
    <div class="contact">
      <p class="person"><span class="person-name">Miles T. Fenwick</span><span class="person-sep">|</span><span class="person-title">Principal</span></p>
      <p class="address">PO Box 48217 Brookvale, NC 27000</p>
      <div class="contact-row">
        <span class="contact-item"><svg viewBox="0 0 12 12"><path d="M2.5 1 L4.5 1 L5.5 3.5 L4.2 4.5 Q5 6.8 7.5 7.8 L8.5 6.5 L11 7.5 L11 9.5 Q10 11 8 10.7 Q2 9 1.2 3 Q1 1.5 2.5 1Z"/></svg>123-456-7890</span>
        <span class="contact-item"><svg viewBox="0 0 12 12"><rect x="3" y="0.5" width="6" height="11" rx="1"/><rect x="4" y="2" width="4" height="6.5" fill="#fff"/></svg>919-555-0147</span>
        <span class="contact-item"><svg viewBox="0 0 12 12"><rect x="3" y="0.5" width="6" height="4"/><rect x="0.5" y="4" width="11" height="6" rx="1"/><rect x="3" y="8" width="6" height="3.5" fill="#fff" stroke="#1f3a6e"/></svg>123-456-7890</span>
      </div>
      <div class="contact-row">
        <span class="contact-item"><svg viewBox="0 0 12 12"><circle cx="6" cy="6" r="5.5"/></svg>miles@corwinashdale-example.com</span>
        <span class="contact-item"><svg viewBox="0 0 12 12"><circle cx="6" cy="6" r="5.5"/></svg>www.corwinashdale-example.com</span>
      </div>
    </div>
  </section>

  <section class="card card-back">
    <div class="back-mark">Corwin Ashdale</div>
  </section>
</body>
</html>
```